Business Intelligence/Analytics Technology Company Business Card

We are a higher-end enterprise software development company working with Retailer POS data to provide business intelligence and analytical services to fortune 500 companies.

I have an immediate need for a professional/thick/bold business card. The same design aspects will spiral into more media such as flyers/folders/etc...

Our website is www.brenvolq.com for our product.

I like "Clean" designs if that makes sense, not a lot of "stuff".

The uploaded files, the A logo with the box is the style we're leaning towards, but the A logo without the blue box is all good too... get creative.

Target Market(s)

Executives of large companies, down to VP level..

Industry/Entity Type

Software

Requirements
Must have
• I'm wanting a thick designer like business card.

I think we're going to change our logo to a more quillmesh 8 looking style... http://www.brenvolq.com/card.ai as an example of our current business card.

The winner will also have knowledge of where i can get these things printed.
Nice to have
• Blue-ish color scheme? I'm open to anything. Our Competition is Red, and another is Green. So we'll stick with the Blue.

```html
<!DOCTYPE html>
<html lang="en">
<head>
<meta charset="utf-8">
<title>Brenvolq Business Card</title>
<link rel="stylesheet" href="https://fonts.googleapis.com/css2?family=Open+Sans:wght@300;400;600;700&display=swap">
<style>
  :root {
    --blue-deep: #0b3f8c;
    --blue-mid: #0f5eb0;
    --blue-bright: #1776c4;
    --grey-band: #8c8f94;
    --grey-light: #d4d6d9;
    --ink: #2b2b2b;
    --ink-soft: #4a4a4a;
    --paper: #ffffff;
    --stage: #eceef0;
  }
  * { margin: 0; padding: 0; box-sizing: border-box; }
  html, body { width: 1200px; height: 900px; overflow: hidden; }
  body {
    background: var(--stage);
    font-family: "Open Sans", Arial, sans-serif;
    display: flex;
    align-items: center;
    justify-content: center;
    gap: 40px;
  }
  .card {
    position: relative;
    width: 540px;
    height: 309px;
    overflow: hidden;
    box-shadow: 0 4px 14px rgba(0,0,0,0.18);
  }

  /* Front */
  .card-front {
    background: linear-gradient(135deg, var(--blue-bright) 0%, var(--blue-mid) 45%, var(--blue-deep) 100%);
    color: var(--paper);
  }
  .front-glow {
    position: absolute;
    inset: 0;
    background: radial-gradient(ellipse 60% 70% at 70% 35%, rgba(255,255,255,0.10), rgba(255,255,255,0) 70%);
  }
  .front-brand {
    position: absolute;
    left: 0; right: 0;
    top: 108px;
    text-align: center;
  }
  .front-name {
    font-size: 34px;
    font-weight: 400;
    letter-spacing: 14px;
    padding-left: 14px;
  }
  .front-tagline {
    font-size: 12px;
    font-weight: 600;
    margin-top: 4px;
  }
  .front-web {
    position: absolute;
    left: 0; right: 0;
    bottom: 58px;
    text-align: center;
    font-size: 13px;
    letter-spacing: 0.5px;
  }

  /* Back */
  .card-back { background: var(--paper); color: var(--ink); }
  .back-shapes { position: absolute; inset: 0; }
  .back-brand { position: absolute; left: 40px; top: 52px; }
  .back-name {
    font-size: 28px;
    font-weight: 400;
    letter-spacing: 11px;
    color: var(--ink);
  }
  .back-tagline { font-size: 10.5px; font-weight: 700; color: var(--ink); margin-top: 2px; }
  .divider {
    position: absolute;
    left: 312px; top: 150px;
    width: 60px; height: 1px;
    background: var(--grey-band);
    transform: rotate(20deg);
  }
  .person { position: absolute; left: 40px; top: 172px; }
  .person-name { font-size: 18px; font-weight: 700; color: var(--ink); line-height: 1.1; }
  .person-title { font-size: 11px; font-weight: 700; color: var(--ink-soft); }
  .contact-list { list-style: none; margin-top: 10px; }
  .contact-list li {
    display: flex; align-items: center; gap: 7px;
    font-size: 11.5px; color: var(--ink-soft); line-height: 1.5;
  }
  .contact-list svg { width: 10px; height: 10px; flex: none; }
  .company { position: absolute; left: 340px; top: 46px; }
  .company-name { font-size: 11px; font-weight: 700; color: var(--ink); margin-bottom: 2px; }
  .address { font-size: 11px; color: var(--ink-soft); line-height: 1.35; padding-left: 17px; position: relative; }
  .address svg { position: absolute; left: 0; top: 2px; width: 10px; height: 10px; }
  .company .contact-list { margin-top: 6px; }
  .back-web {
    position: absolute;
    right: 30px; bottom: 16px;
    font-size: 12px;
    color: var(--paper);
    letter-spacing: 0.4px;
  }
</style>
</head>
<body>

  <section class="card card-front" aria-label="Card front">
    <div class="front-glow"></div>
    <div class="front-brand">
      <div class="front-name">BRENVOLQ</div>
      <div class="front-tagline">Brenvolq . Vantix . Retail health</div>
    </div>
    <div class="front-web">www.brenvolq.com</div>
  </section>

  <section class="card card-back" aria-label="Card back">
    <svg class="back-shapes" viewBox="0 0 540 309" preserveAspectRatio="none">
      <path d="M0 309 L0 262 C190 300 400 250 540 96 L540 128 C450 240 330 290 210 309 Z" fill="var(--grey-light)"/>
      <path d="M120 309 C280 300 430 240 540 128 L540 150 C450 250 330 296 250 309 Z" fill="var(--grey-band)"/>
      <path d="M250 309 C340 296 460 250 540 150 L540 309 Z" fill="var(--blue-mid)"/>
      <path d="M300 309 C380 298 480 258 540 190 L540 309 Z" fill="var(--blue-deep)" opacity="0.35"/>
    </svg>

    <div class="back-brand">
      <div class="back-name">BRENVOLQ</div>
      <div class="back-tagline">Brenvolq . Vantix . Retail health</div>
    </div>

    <div class="divider"></div>

    <div class="person">
      <div class="person-name">Dorian Kessler</div>
      <div class="person-title">Business Director</div>
      <ul class="contact-list">
        <li>
          <svg viewBox="0 0 10 10"><rect x="0.5" y="1.5" width="9" height="7" fill="var(--blue-mid)"/><path d="M0.5 1.5 L5 5.5 L9.5 1.5" stroke="#fff" fill="none" stroke-width="1"/></svg>
          dorian@brenvolq.com
        </li>
        <li>
          <svg viewBox="0 0 10 10"><rect x="2" y="0.5" width="6" height="9" rx="1" fill="none" stroke="var(--blue-mid)" stroke-width="1.2"/></svg>
          555.236.0142
        </li>
      </ul>
    </div>

    <div class="company">
      <div class="company-name">Brenvolq Technology Group, Inc</div>
      <div class="address">
        <svg viewBox="0 0 10 10"><path d="M5 0.5 L9.5 5 L8 5 L8 9.5 L2 9.5 L2 5 L0.5 5 Z" fill="var(--blue-mid)"/></svg>
        1450 Halvern Ave<br>Suite 302<br>Marlow, AR 70000
      </div>
      <ul class="contact-list">
        <li>
          <svg viewBox="0 0 10 10"><path d="M2 0.5 L4 3 L3 4.2 C3.6 5.6 4.4 6.4 5.8 7 L7 6 L9.5 8 L8.3 9.5 C4.5 9.2 0.8 5.5 0.5 1.7 Z" fill="var(--blue-mid)"/></svg>
          555.899.0171
        </li>
        <li>
          <svg viewBox="0 0 10 10"><rect x="1" y="3" width="8" height="6.5" fill="var(--blue-mid)"/><rect x="2.5" y="0.5" width="5" height="3" fill="none" stroke="var(--blue-mid)"/></svg>
          555.899.0188
        </li>
      </ul>
    </div>

    <div class="back-web">www.brenvolq.com</div>
  </section>

</body>
</html>
```